Upmarket Bathroom and Kitchen ware supplier needs a classy business card design

We are a company based in Fiji, we sell plumbing ware (Kitchen and bathroom taps, Basins,showers, toilets etc) through up market show rooms to individuals and directly through Architects and designers of resorts and holiday houses for new builds and renovations. we are wanting to upgrade our over all look and brand. we are starting with a new logo but will be rebranding the whole business. This project is for a business card design for my management and tales team I would like it to be dark, classy and interesting

Target Market(s)

Resort directors and Management, High end holiday home owners

Contact Information for Business Card

Marcus Tellen
Director
+64219473815

Colors

Designer to choose colors to be used in the design.

Requirements
Must have
• Must have an upmarket appearance I like darker charcoal shades but will be guided by the designers
• Please any catch phrases like "Crafting remarkable living rooms" this belongs tpo one of our suppliers so can not be used.
Nice to have
• Double sided, so front dedicated to logo provided and back info about the business and the person.

```html
<!DOCTYPE html>
<html lang="en">
<head>
<meta charset="utf-8">
<title>Halvane Interiors – Business Card</title>
<link rel="stylesheet" href="https://fonts.googleapis.com/css2?family=Montserrat:wght@300&family=Signika:wght@400;600&family=Permanent+Marker&display=swap">
<style>
  :root {
    --backdrop: #d7e1e3;
    --charcoal: #161616;
    --charcoal-light: #2a2a2a;
    --orange: #f26a1b;
    --white: #ffffff;
    --photo-warm: #8a4a26;
    --photo-dark: #2b2522;
    --product-bg: #e9e9e9;
  }
  * { box-sizing: border-box; margin: 0; padding: 0; }
  html, body { width: 1200px; height: 1200px; overflow: hidden; }
  body { background: var(--backdrop); position: relative; font-family: "Signika", sans-serif; }

  .card {
    position: absolute;
    overflow: hidden;
    background: radial-gradient(ellipse at 50% 45%, var(--charcoal-light) 0%, var(--charcoal) 65%);
  }
  .card--front { left: 258px; top: 72px; width: 694px; height: 465px; }
  .card--back { left: 258px; top: 637px; width: 703px; height: 471px; }

  .frame { position: absolute; }
  .frame--outer { left: 30px; top: 30px; width: 627px; height: 405px; border: 1.5px solid var(--white); }
  .frame--inner { left: 43px; top: 44px; width: 602px; height: 377px; border: 1.5px solid var(--orange); }

  .brand {
    position: absolute;
    display: flex;
    align-items: center;
    color: var(--white);
    font-family: "Montserrat", sans-serif;
    font-weight: 300;
    letter-spacing: 0.28em;
    white-space: nowrap;
  }
  .brand__dot { border: 1.5px solid var(--white); border-radius: 50%; flex: none; }
  .brand--front { left: 0; right: 0; top: 206px; justify-content: center; font-size: 26px; gap: 18px; }
  .brand--front .brand__dot { width: 44px; height: 44px; }
  .brand--back { left: 40px; top: 76px; font-size: 17px; gap: 12px; }
  .brand--back .brand__dot { width: 30px; height: 30px; }

  .rule { position: absolute; left: 0; background: var(--orange); }
  .rule--thick { top: 152px; width: 414px; height: 3px; }
  .rule--thin { top: 161px; width: 414px; height: 1px; opacity: 0.8; }
  .rule--base { top: 344px; width: 440px; height: 1px; opacity: 0.8; }

  .contact { position: absolute; left: 35px; top: 206px; }
  .contact__name { color: var(--orange); font-weight: 600; font-size: 26px; letter-spacing: 0.06em; }
  .contact__role { color: var(--white); font-size: 16px; margin-top: 6px; }
  .contact__phone { display: flex; align-items: center; gap: 8px; margin-top: 16px; color: var(--white); font-size: 18px; }
  .contact__phone svg { width: 32px; height: 32px; flex: none; }

  .tagline {
    position: absolute; left: 35px; top: 366px;
    color: var(--orange);
    font-family: "Permanent Marker", "Signika", sans-serif;
    font-size: 20px; line-height: 35px;
    text-transform: uppercase;
    white-space: nowrap;
  }

  .feature { position: absolute; left: 0; top: 0; width: 703px; height: 471px; }
</style>
</head>
<body>

  <section class="card card--front" aria-label="Card front">
    <div class="frame frame--outer"></div>
    <div class="frame frame--inner"></div>
    <div class="brand brand--front"><span class="brand__dot"></span>HALVANE INTERIORS</div>
  </section>

  <section class="card card--back" aria-label="Card back">
    <div class="brand brand--back"><span class="brand__dot"></span>HALVANE INTERIORS</div>
    <div class="rule rule--thick"></div>
    <div class="rule rule--thin"></div>

    <div class="contact">
      <p class="contact__name">MARCUS TELLEN</p>
      <p class="contact__role">Director</p>
      <p class="contact__phone">
        <svg viewBox="0 0 32 32" aria-hidden="true">
          <circle cx="16" cy="16" r="16" fill="var(--orange)"/>
          <path d="M12.5 9.5l2 3.2-1.4 1.4c.7 1.8 2 3.1 3.8 3.8l1.4-1.4 3.2 2-1.2 2.6c-4.8-.3-9.2-4.7-9.5-9.5z" fill="var(--white)"/>
        </svg>
        +64219473815
      </p>
    </div>

    <div class="rule rule--base"></div>
    <p class="tagline">It is individuals and directly<br>through architects and designers</p>

    <svg class="feature" viewBox="0 0 703 471">
      <defs>
        <linearGradient id="photoTone" x1="0" y1="0" x2="1" y2="1">
          <stop offset="0" stop-color="var(--photo-warm)"/>
          <stop offset="1" stop-color="var(--photo-dark)"/>
        </linearGradient>
        <clipPath id="photoClip"><circle cx="700" cy="255" r="262"/></clipPath>
      </defs>
      <rect x="420" y="0" width="283" height="471" fill="url(#photoTone)" clip-path="url(#photoClip)"
            role="img" aria-label="Photo of a modern timber-clad house with the director in a suit pointing at the products"/>
      <circle cx="700" cy="255" r="266" fill="none" stroke="var(--orange)" stroke-width="9"/>
      <path d="M540 40 A320 320 0 0 1 650 5" fill="none" stroke="var(--orange)" stroke-width="4"/>
      <g fill="var(--product-bg)" stroke="var(--orange)" stroke-width="4">
        <circle cx="501" cy="69" r="40" role="img" aria-label="Product photo: kitchen mixer tap"/>
        <circle cx="458" cy="151" r="40" role="img" aria-label="Product photo: black vessel basin"/>
        <circle cx="448" cy="245" r="40" role="img" aria-label="Product photo: black shower head"/>
        <circle cx="472" cy="341" r="40" role="img" aria-label="Product photo: black toilet"/>
      </g>
    </svg>
  </section>

</body>
</html>
```